Business Card Design needed for logo design project

This project is linked to Corvelle acupuncture - Odile RAVINEAU.

Our company needs a Business Card Design. Please refer to our original project in the link above.

Industry/Entity Type

Business

```html
<!DOCTYPE html>
<html lang="en">
<head>
<meta charset="utf-8">
<title>Corvelle acupuncture – Business Card</title>
<link rel="stylesheet" href="https://fonts.googleapis.com/css2?family=Cinzel:wght@700&family=Courier+Prime:wght@700&family=Pathway+Gothic+One&family=Share+Tech+Mono&family=Yanone+Kaffeesatz:wght@400&display=swap">
<style>
  :root {
    --bg: #2b2a27;
    --heading-blue: #1a80c0;
    --white: #ffffff;
    --cream: #f2f2dc;
    --navy: #0b1f3a;
    --blue: #0b80c0;
    --blue-strip: #0e84c2;
    --blue-fold: #155a80;
    --green: #8fcf6a;
    --green-fold: #6aa74e;
    --orange: #f0a52e;
    --orange-fold: #c98320;
    --red: #e2333f;
    --red-fold: #b42430;
  }
  html, body {
    margin: 0;
    padding: 0;
    width: 1200px;
    height: 900px;
    overflow: hidden;
    background: var(--bg);
  }
  .card {
    position: relative;
    width: 1200px;
    height: 900px;
    background: var(--bg);
    overflow: hidden;
  }
  .card-shapes {
    position: absolute;
    inset: 0;
  }
  .text {
    position: absolute;
    margin: 0;
    white-space: nowrap;
  }
  .holder-name {
    left: 0; width: 1200px; top: 16px;
    text-align: center;
    font-family: "Cinzel", serif;
    font-weight: 700;
    font-size: 66px;
    color: var(--heading-blue);
    padding-left: 20px;
  }
  .holder-role {
    left: 0; width: 1200px; top: 100px;
    text-align: center;
    font-family: "Cinzel", serif;
    font-weight: 700;
    font-size: 50px;
    color: var(--heading-blue);
    padding-left: 32px;
  }
  .address {
    left: 0; width: 1200px; top: 210px;
    text-align: center;
    font-family: "Pathway Gothic One", sans-serif;
    font-size: 52px;
    color: var(--white);
    padding-left: 0;
    text-indent: -50px;
  }
  .brand-name {
    left: 0; width: 128px; top: 584px;
    text-align: center;
    font-family: "Yanone Kaffeesatz", sans-serif;
    font-size: 26px;
    color: var(--white);
  }
  .practitioner {
    left: 164px; width: 348px; top: 462px;
    text-align: center;
    font-family: "Yanone Kaffeesatz", sans-serif;
    font-size: 72px;
    line-height: 1;
    color: var(--white);
  }
  .tagline {
    left: 164px; width: 348px; top: 598px;
    text-align: center;
    font-family: "Courier Prime", monospace;
    font-weight: 700;
    font-size: 36px;
    line-height: 50px;
    color: var(--navy);
  }
  .contact {
    left: 610px;
    font-size: 44px;
    line-height: 1;
  }
  .contact-phone {
    top: 424px;
    font-family: "Share Tech Mono", monospace;
    letter-spacing: 4px;
    color: var(--cream);
  }
  .contact-email {
    top: 563px;
    font-family: "Pathway Gothic One", sans-serif;
    color: var(--white);
  }
  .contact-web {
    top: 700px;
    font-family: "Pathway Gothic One", sans-serif;
    color: var(--white);
  }
</style>
</head>
<body>
<main class="card">
  <svg class="card-shapes" width="1200" height="900" viewBox="0 0 1200 900" aria-hidden="true">
    <!-- header rules -->
    <line x1="226" y1="196" x2="974" y2="196" stroke="var(--white)" stroke-width="3"/>
    <line x1="226" y1="296" x2="974" y2="296" stroke="var(--white)" stroke-width="3"/>

    <!-- left folded ribbon -->
    <rect x="0" y="364" width="128" height="366" fill="var(--blue-strip)"/>
    <polygon points="128,364 164,400 164,776 128,730" fill="var(--blue-fold)"/>
    <rect x="164" y="400" width="348" height="376" fill="var(--blue)"/>

    <!-- brand mark circle -->
    <circle cx="62" cy="530" r="40" fill="var(--white)" stroke="var(--blue-fold)" stroke-width="6"/>

    <!-- phone ribbon -->
    <rect x="534" y="398" width="528" height="98" fill="var(--green)"/>
    <polygon points="1062,398 1110,360 1110,458 1062,496" fill="var(--green-fold)"/>
    <rect x="1110" y="360" width="90" height="98" fill="var(--green)"/>

    <!-- email ribbon -->
    <rect x="534" y="538" width="528" height="98" fill="var(--orange)"/>
    <polygon points="1062,538 1110,500 1110,598 1062,636" fill="var(--orange-fold)"/>
    <rect x="1110" y="500" width="90" height="98" fill="var(--orange)"/>

    <!-- web ribbon -->
    <rect x="534" y="676" width="528" height="98" fill="var(--red)"/>
    <polygon points="1062,676 1110,638 1110,736 1062,774" fill="var(--red-fold)"/>
    <rect x="1110" y="638" width="90" height="98" fill="var(--red)"/>

    <!-- phone icon -->
    <g class="icon-phone" fill="var(--white)">
      <path d="M1138,392 h34 a6,6 0 0 1 6,6 v6 h-10 v-4 h-26 v4 h-10 v-6 a6,6 0 0 1 6,-6 z"/>
      <path d="M1142,406 h26 l6,24 h-38 z"/>
      <circle cx="1155" cy="418" r="6" fill="var(--green)"/>
    </g>

    <!-- envelope icon -->
    <g class="icon-mail">
      <rect x="1134" y="534" width="42" height="30" fill="var(--white)"/>
      <polyline points="1134,534 1155,552 1176,534" fill="none" stroke="var(--orange)" stroke-width="3"/>
      <line x1="1134" y1="564" x2="1149" y2="549" stroke="var(--orange)" stroke-width="2"/>
      <line x1="1176" y1="564" x2="1161" y2="549" stroke="var(--orange)" stroke-width="2"/>
    </g>

    <!-- globe icon -->
    <g class="icon-web" fill="none" stroke="var(--white)" stroke-width="3">
      <circle cx="1155" cy="687" r="21"/>
      <ellipse cx="1155" cy="687" rx="9" ry="21"/>
      <line x1="1155" y1="666" x2="1155" y2="708"/>
      <line x1="1134" y1="687" x2="1176" y2="687"/>
      <line x1="1138" y1="676" x2="1172" y2="676"/>
      <line x1="1138" y1="698" x2="1172" y2="698"/>
    </g>
  </svg>

  <h1 class="text holder-name">Name</h1>
  <p class="text holder-role">Designation</p>
  <p class="text address">address here</p>

  <p class="text brand-name">Corvelle</p>
  <p class="text practitioner">Odile RAVINEAU</p>
  <p class="text tagline">Get balanced<br>and be healthy</p>

  <p class="text contact contact-phone">763-555-0187</p>
  <p class="text contact contact-email">info@corvelle.com</p>
  <p class="text contact contact-web">www.corvelle.com</p>
</main>
</body>
</html>
```